Business Card Design for company

We want new business cards. We'd like something different-- yet still highly professional. Our tagline is Providing leadership, delivering success. Stock photos are ok, as long as they are relevant and look upscale.

Target Market(s)

Architecture/Business Management Consulting/Engineering Consulting

Contact Information for Business Card

dark gray background with pops of blue might be good, but you tell me. You're the designers. Rounded corners might be nice, but again, you tell me.

Font styles to use
Serif
Sans Serif

Colors
3276b5
5c5c5c
9d9d9d
fbfbfb

Requirements
Nice to have
• Something different, but still very professional.

```html
<!DOCTYPE html>
<html lang="en">
<head>
<meta charset="utf-8">
<title>Torvane Group Business Card</title>
<link rel="stylesheet" href="https://fonts.googleapis.com/css2?family=Poppins:wght@400;500;600;700&display=swap">
<style>
  :root {
    --blue: #3276b5;
    --blue-deep: #2a67a3;
    --blue-light: #4a8cc8;
    --gray-dark: #5c5c5c;
    --gray-mid: #9d9d9d;
    --paper: #fbfbfb;
    --stage: #e9edf1;
    --white: #ffffff;
  }
  * { margin: 0; padding: 0; box-sizing: border-box; }
  html, body {
    width: 1200px; height: 928px; overflow: hidden;
    background: var(--stage);
    font-family: "Poppins", sans-serif;
  }
  .stage { position: relative; width: 1200px; height: 928px; }
  .card {
    position: absolute; width: 700px; height: 400px;
    border-radius: 26px; overflow: hidden;
    box-shadow: 0 10px 30px rgba(0,0,0,0.15);
  }
  /* Front */
  .card-front {
    left: 250px; top: 40px;
    background: linear-gradient(160deg, var(--blue-light), var(--blue) 55%, var(--blue-deep));
  }
  .world-map {
    position: absolute; left: 60px; top: 30px; width: 600px; height: 300px;
    border-radius: 40% 50% 45% 40%;
    background: radial-gradient(ellipse at center, rgba(255,255,255,0.16), rgba(255,255,255,0.04) 70%, transparent);
  }
  .front-brand {
    position: absolute; left: 0; right: 0; top: 150px; text-align: center;
    color: var(--white); font-weight: 600; font-size: 54px; letter-spacing: 2px;
  }
  .front-web {
    position: absolute; left: 0; right: 0; top: 240px; text-align: center;
    color: var(--white); font-size: 15px; font-weight: 400; letter-spacing: 0.5px;
  }
  /* Back */
  .card-back { left: 250px; top: 488px; background: var(--paper); }
  .card-back .swoosh { position: absolute; inset: 0; }
  .back-brand {
    position: absolute; left: 38px; top: 62px;
    color: var(--blue); font-weight: 600; font-size: 46px; line-height: 1.05; letter-spacing: 1px;
  }
  .holder { position: absolute; right: 40px; top: 34px; text-align: right; }
  .holder-name { color: var(--blue); font-weight: 700; font-size: 26px; letter-spacing: 0.5px; }
  .holder-title { color: var(--gray-dark); font-size: 15px; margin-top: 2px; }
  .address {
    position: absolute; right: 40px; top: 196px; text-align: right;
    color: var(--white); font-size: 15px; line-height: 1.5;
  }
  .contacts {
    position: absolute; right: 40px; top: 262px; list-style: none;
    color: var(--white); font-size: 15px;
  }
  .contacts li {
    display: flex; justify-content: flex-end; align-items: center;
    gap: 10px; height: 27px;
  }
  .contacts svg { width: 16px; height: 16px; flex: none; }
  .tagline {
    position: absolute; left: 38px; bottom: 34px; list-style: none;
    color: var(--white); font-size: 16px; font-weight: 500; line-height: 1.6;
  }
  .tagline li::before {
    content: ""; display: inline-block; width: 8px; height: 8px;
    background: var(--white); margin-right: 8px; vertical-align: middle;
  }
</style>
</head>
<body>
<main class="stage">
  <section class="card card-front">
    <div class="world-map" role="img" aria-label="Faint world map in light blue tones"></div>
    <div class="front-brand">TORVANE GROUP</div>
    <div class="front-web">www.torvanegroup.com</div>
  </section>

  <section class="card card-back">
    <svg class="swoosh" viewBox="0 0 700 400" preserveAspectRatio="none" aria-hidden="true">
      <path d="M0,232 C190,290 380,150 700,112 L700,150 C400,180 200,320 0,270 Z" fill="var(--gray-mid)" opacity="0.55"/>
      <path d="M0,262 C200,312 400,176 700,140" fill="none" stroke="var(--gray-dark)" stroke-width="4"/>
      <path d="M0,280 C200,330 400,196 700,156 L700,400 L0,400 Z" fill="var(--blue)"/>
    </svg>

    <div class="back-brand">TORVANE<br>GROUP</div>

    <div class="holder">
      <div class="holder-name">DANIEL HART</div>
      <div class="holder-title">Resident Manager</div>
    </div>

    <div class="address">418 W Harbor Ave. Ste 210<br>Easton, VA 23411</div>

    <ul class="contacts">
      <li>+1 555.201.4830
        <svg viewBox="0 0 24 24"><path fill="#fff" d="M6.6 10.8a15.1 15.1 0 0 0 6.6 6.6l2.2-2.2c.3-.3.7-.4 1-.2 1.1.4 2.3.6 3.6.6.6 0 1 .4 1 1V20c0 .6-.4 1-1 1A17 17 0 0 1 3 4c0-.6.4-1 1-1h3.5c.6 0 1 .4 1 1 0 1.3.2 2.5.6 3.6.1.3 0 .7-.2 1z"/></svg>
      </li>
      <li>+1 555.461.7702
        <svg viewBox="0 0 24 24"><path fill="#fff" d="M7 3h10v4H7zM4 8h16a2 2 0 0 1 2 2v6h-4v5H6v-5H2v-6a2 2 0 0 1 2-2zm4 8v3h8v-3z"/></svg>
      </li>
      <li>info@torvanegroup.com
        <svg viewBox="0 0 24 24"><path fill="none" stroke="#fff" stroke-width="2" d="M3 5h18v14H3zM3 6l9 7 9-7"/></svg>
      </li>
      <li>www.torvanegroup.com
        <svg viewBox="0 0 24 24"><g fill="none" stroke="#fff" stroke-width="2"><circle cx="12" cy="12" r="9"/><path d="M3 12h18M12 3c3 3 3 15 0 18M12 3c-3 3-3 15 0 18"/></g></svg>
      </li>
    </ul>

    <ul class="tagline">
      <li>Providing leadership</li>
      <li>Delivering success</li>
    </ul>
  </section>
</main>
</body>
</html>
```